tarvo fulfilment website design wordpress

I'm looking for a website design (WordPress) for an order fulfillment company. the company is a micro-fulfillment company that offers the following services: inventory management, order fulfillment, returns, and storage. the site must have a multilanguage feature.

the website must look modern and professional. Also, the website should not look like it came from a template.

sample site:
https://parlo-dep.nl/fulfilment-tarieven/
https://www.zentrik.com/

Target Market(s)

ecommerce owner

Industry/Entity Type

logistics

Coding

Coded - Design and coding required

Number of Pages Required

5+ page

Colors
0054AA
0677BA
7BADD7
CADEEF
E8F1F8

Requirements
Must have
• multilanguage
Should not have
• look that the design came from a template

```html
<!DOCTYPE html>
<html lang="en">
<head>
<meta charset="utf-8">
<title>Tarvo Fulfilment</title>
<link rel="stylesheet" href="https://fonts.googleapis.com/css2?family=Saira+Semi+Condensed:wght@500;600;700&family=Lato:wght@400;700&display=swap">
<style>
:root{
  --navy:#1d3e66;
  --blue:#0677ba;
  --sky:#4a9be0;
  --field:#6cb1ea;
  --pale:#cadeef;
  --mist:#e8f1f8;
  --ink:#2a2f3a;
  --grey:#5b6270;
  --white:#ffffff;
}
*{box-sizing:border-box;margin:0;padding:0}
html,body{width:1200px;height:4011px;overflow:hidden;background:var(--white)}
body{font-family:"Lato",sans-serif;color:var(--ink)}
.page{position:relative;width:1200px;height:4011px;overflow:hidden}
.abs{position:absolute}
.head{font-family:"Saira Semi Condensed",sans-serif}
.center{text-align:center}

.topbar{left:0;top:0;width:1200px;height:59px;background:var(--navy)}
.topbar .item{top:20px;font-size:14px;color:#8fc0ee;font-weight:700}
.topbar .dot{top:20px;width:18px;height:18px;border-radius:50%;border:1.5px solid #8fc0ee}

.nav{left:0;top:59px;width:1200px;height:103px;background:var(--white)}
.brand{font-family:"Saira Semi Condensed",sans-serif;font-weight:700;color:var(--navy);letter-spacing:.5px;white-space:nowrap}
.brand-square{background:var(--navy)}
.menu a{position:absolute;top:43px;font-size:14px;color:var(--ink);text-decoration:none}
.menu .active{color:var(--navy);font-weight:700;text-decoration:underline;text-underline-offset:5px}
.btn{display:flex;align-items:center;justify-content:center;font-family:"Saira Semi Condensed",sans-serif;font-weight:700;border-radius:6px;white-space:nowrap}
.btn-dark{background:var(--navy);color:var(--white)}
.btn-light{background:var(--white);color:var(--navy)}

.hero-text .eyebrow{font-family:"Saira Semi Condensed",sans-serif;font-weight:700;font-size:17px;letter-spacing:1.5px;color:var(--sky)}
.hero-text .line{font-family:"Saira Semi Condensed",sans-serif;font-weight:600;font-size:31px;color:var(--white);white-space:nowrap}
.hero-text .line.accent{color:var(--sky)}

.card{background:var(--white);box-shadow:0 6px 22px rgba(20,40,70,.15);border-left:6px solid var(--sky)}
.range{position:absolute;top:123px;height:48px;border:1.5px solid var(--navy);display:flex;align-items:center;justify-content:center;gap:10px;font-size:14px;color:var(--navy);font-weight:700;white-space:nowrap}

.step-title{font-family:"Saira Semi Condensed",sans-serif;font-weight:700;font-size:19px;color:var(--navy)}
.small{font-size:12.5px;line-height:23px;color:var(--grey)}

.eyebrow-blue{font-family:"Saira Semi Condensed",sans-serif;font-weight:600;font-size:19px;color:var(--sky);letter-spacing:.5px}
.section-title{font-family:"Saira Semi Condensed",sans-serif;font-weight:700;font-size:34px;color:var(--navy);white-space:nowrap}
.hex{clip-path:polygon(0 15%,50% 0,100% 15%,100% 85%,50% 100%,0 85%)}
.circle-btn{width:62px;height:62px;border-radius:50%;background:var(--white);box-shadow:0 3px 10px rgba(0,0,0,.15);display:flex;align-items:center;justify-content:center}
.service-title{font-family:"Saira Semi Condensed",sans-serif;font-weight:700;font-size:22px;color:var(--navy)}
.body{font-size:14.5px;line-height:26.5px;color:var(--grey)}
.link{font-size:15px;color:var(--navy);text-decoration:underline;font-weight:700}

.field{background:var(--field);color:var(--navy);font-size:13.5px;padding:14px 18px}
.footer-title{font-family:"Saira Semi Condensed",sans-serif;font-weight:700;font-size:19px;color:var(--navy)}
.footer-list li{list-style:none;font-size:14.5px;color:var(--ink);height:34px;display:flex;align-items:center;gap:12px}
.social{width:33px;height:33px;border-radius:50%;background:var(--navy)}
</style>
</head>
<body>
<div class="page">

  <div class="abs topbar">
    <svg class="abs" style="left:110px;top:20px" width="18" height="18" viewBox="0 0 24 24"><path d="M6.6 10.8a15.1 15.1 0 0 0 6.6 6.6l2.2-2.2c.3-.3.7-.4 1-.2 1.1.4 2.3.6 3.6.6.6 0 1 .4 1 1V20c0 .6-.4 1-1 1A17 17 0 0 1 3 4c0-.6.4-1 1-1h3.5c.6 0 1 .4 1 1 0 1.3.2 2.5.6 3.6.1.3 0 .7-.2 1z" fill="#8fc0ee"/></svg>
    <div class="abs item" style="left:166px">Call:+1 555 010 0199</div>
    <svg class="abs" style="left:344px;top:21px" width="18" height="14" viewBox="0 0 20 14"><rect width="20" height="14" rx="2" fill="#8fc0ee"/><path d="M1 1l9 7 9-7" stroke="#1d3e66" stroke-width="1.6" fill="none"/></svg>
    <div class="abs item" style="left:402px">Mail:info@tarvofulfilment.com</div>
    <div class="abs dot" style="left:951px"></div>
    <div class="abs dot" style="left:991px"></div>
    <div class="abs dot" style="left:1031px"></div>
    <div class="abs dot" style="left:1071px"></div>
  </div>

  <div class="abs nav">
    <div class="abs brand-square" style="left:130px;top:19px;width:34px;height:34px"></div>
    <div class="abs brand" style="left:109px;top:64px;font-size:21px">TARVO FULFILMENT</div>
    <nav class="menu">
      <a class="active" style="left:428px">HOME</a>
      <a style="left:507px">ABOUT US</a>
      <a style="left:613px">SERVICE</a>
      <a style="left:706px">TESTIMONIALS</a>
    </nav>
    <div class="abs btn btn-dark" style="left:838px;top:29px;width:130px;height:45px;font-size:14.5px">CONTACT US</div>
    <div class="abs head" style="left:1037px;top:42px;font-size:15px;font-weight:700;color:var(--navy)">EN</div>
    <svg class="abs" style="left:1064px;top:39px" width="24" height="24" viewBox="0 0 24 24" fill="none" stroke="var(--navy)" stroke-width="1.6"><circle cx="12" cy="12" r="10"/><ellipse cx="12" cy="12" rx="4.5" ry="10"/><path d="M2 12h20M4 6.5h16M4 17.5h16"/></svg>
  </div>

  <svg class="abs" style="left:0;top:162px" width="1200" height="776" viewBox="0 0 1200 776">
    <path d="M0 0H1200V650L810 720 600 776 390 720 0 610Z" fill="var(--navy)"/>
  </svg>
  <div class="abs hero-text" style="left:112px;top:256px">
    <div class="eyebrow">WELCOME TO TARVO FULFILMENT</div>
    <div class="line" style="margin-top:18px">ECOMMERCE BUSINESSES TO</div>
    <div class="line accent" style="margin-top:8px">STORE THEIR INVENTORY</div>
    <div class="line" style="margin-top:8px">CLOSER TO THE END CONSUMER</div>
    <div style="margin-top:18px;font-size:14px;color:var(--white)">So they can reduce cost and transit times</div>
  </div>
  <div class="abs btn btn-light" style="left:112px;top:511px;width:150px;height:51px;font-size:17px">GET STARTED</div>
  <div class="abs" role="img" aria-label="Isometric illustration of warehouse shelving, a scanner, parcels and workers" style="left:576px;top:184px;width:599px;height:416px;background:radial-gradient(ellipse at 55% 50%,#a9c8e8 0%,#6f9ccb 45%,rgba(29,62,102,0) 72%)"></div>

  <div class="abs card" style="left:148px;top:640px;width:906px;height:240px">
    <div class="abs head center" style="left:0;top:28px;width:900px;font-size:24px;font-weight:700;color:var(--navy)">FIND YOUR FULFILLMENT SOLUTION</div>
    <div class="abs center" style="left:0;top:76px;width:900px;font-size:15px;color:var(--grey)">Itaque earum rerum hic tenetur a sapiente delectus, ut aut reiciendis voluptatibus</div>
    <div class="range" style="left:73px;width:109px">1 - 100 <span style="color:var(--sky)">&#8594;</span></div>
    <div class="range" style="left:202px;width:131px">101 - 500 <span style="color:var(--sky)">&#8594;</span></div>
    <div class="range" style="left:349px;width:148px">501 - 1,001 <span style="color:var(--sky)">&#8594;</span></div>
    <div class="range" style="left:515px;width:162px">1,001 - 5,001 <span style="color:var(--sky)">&#8594;</span></div>
    <div class="range" style="left:694px;width:125px">5,001 + <span style="color:var(--sky)">&#8594;</span></div>
    <div class="abs center" style="left:0;top:199px;width:900px;font-size:13.5px;font-weight:700;color:var(--sky)">Maiores alias consequatur aut perferendis doloribus?</div>
  </div>

  <div class="abs head center" style="left:150px;top:1000px;width:900px;font-size:22.5px;font-weight:600;line-height:41px;color:var(--navy)">Whether you’re a startup or a global enterprise, we can help you unlock your full potential with our eCommerce fulfilment services.</div>

  <div class="abs" role="img" aria-label="Illustration of a worker with a checklist and boxes" style="left:145px;top:1108px;width:140px;height:137px;border-radius:8px;background:linear-gradient(135deg,#d7ecf5,#f3c29b)"></div>
  <div class="abs" role="img" aria-label="Illustration of a figure pushing a hand truck with a parcel" style="left:402px;top:1108px;width:140px;height:137px;border-radius:8px;background:linear-gradient(135deg,#eeeeee,#c9b08a)"></div>
  <div class="abs" role="img" aria-label="Illustration of a delivery courier carrying a box" style="left:658px;top:1108px;width:140px;height:137px;border-radius:8px;background:linear-gradient(135deg,#f2d6d6,#e0475a)"></div>
  <div class="abs" role="img" aria-label="Illustration of a parcel handed over at a front door" style="left:915px;top:1108px;width:140px;height:137px;border-radius:8px;background:linear-gradient(135deg,#e8eef2,#c4873f)"></div>
  <div class="abs center" style="left:120px;top:1262px;width:190px"><div class="step-title">Pickup</div><div class="small" style="margin-top:4px">Lorem ipsum dolor sit amet, elit, sed do eiusmod tempor magna aliqua.</div></div>
  <div class="abs center" style="left:377px;top:1262px;width:190px"><div class="step-title">Packaging</div><div class="small" style="margin-top:4px">Lorem ipsum dolor sit amet, elit, sed do eiusmod tempor magna aliqua.</div></div>
  <div class="abs center" style="left:633px;top:1262px;width:190px"><div class="step-title">Shipping</div><div class="small" style="margin-top:4px">Lorem ipsum dolor sit amet, elit, sed do eiusmod tempor magna aliqua.</div></div>
  <div class="abs center" style="left:890px;top:1262px;width:190px"><div class="step-title">Final customer</div><div class="small" style="margin-top:4px">Lorem ipsum dolor sit amet, elit, sed do eiusmod tempor magna aliqua.</div></div>

  <div class="abs eyebrow-blue center" style="left:0;top:1430px;width:1200px">WHAT WE OFER</div>
  <div class="abs section-title center" style="left:0;top:1464px;width:1200px">OUR SERVICES</div>
  <svg class="abs" style="left:0;top:1580px" width="1200" height="430" viewBox="0 0 1200 430"><path d="M0 20 600 90 1200 0V420L600 350 0 430Z" fill="var(--mist)"/></svg>
  <div class="abs hex" role="img" aria-label="Photo of a warehouse worker with a tablet among boxes" style="left:100px;top:1546px;width:280px;height:207px;background:linear-gradient(135deg,#d6b68c,#8c6a44)"></div>
  <div class="abs hex" role="img" aria-label="Photo of two warehouse workers in safety vests holding a parcel" style="left:454px;top:1546px;width:279px;height:207px;background:linear-gradient(135deg,#a8b8c8,#d88a42)"></div>
  <div class="abs hex" role="img" aria-label="Photo of a parcel being handed between two people" style="left:808px;top:1546px;width:279px;height:207px;background:linear-gradient(135deg,#3f5a7e,#c8a273)"></div>
  <div class="abs circle-btn" style="left:55px;top:1603px"><svg width="20" height="20" viewBox="0 0 20 20"><path d="M17 10H4M9 4 3 10l6 6" stroke="var(--navy)" stroke-width="3" fill="none"/></svg></div>
  <div class="abs circle-btn" style="left:1054px;top:1603px"><svg width="20" height="20" viewBox="0 0 20 20"><path d="M3 10h13M11 4l6 6-6 6" stroke="var(--navy)" stroke-width="3" fill="none"/></svg></div>
  <div class="abs center" style="left:100px;top:1771px;width:280px"><div class="service-title">Inventory Management</div><div class="body" style="margin-top:6px">Lorem ipsum dolor sit amet, consectetur adipiscing elit, sed do eiusmod tempor incididunt ut labore et dolore magna aliqua.</div><div class="link" style="margin-top:8px">Read More</div></div>
  <div class="abs center" style="left:454px;top:1771px;width:280px"><div class="service-title">Order Fulfillment</div><div class="body" style="margin-top:6px">Lorem ipsum dolor sit amet, consectetur adipiscing elit, sed do eiusmod tempor incididunt ut labore et dolore magna aliqua.</div><div class="link" style="margin-top:8px">Read More</div></div>
  <div class="abs center" style="left:808px;top:1771px;width:280px"><div class="service-title">Returns</div><div class="body" style="margin-top:6px">Lorem ipsum dolor sit amet, consectetur adipiscing elit, sed do eiusmod tempor incididunt ut labore et dolore magna aliqua.</div><div class="link" style="margin-top:8px">Read More</div></div>

  <svg class="abs" style="left:0;top:2040px" width="1200" height="360" viewBox="0 0 1200 360"><path d="M0 0 1200 70V300L0 345Z" fill="var(--pale)" opacity=".45"/></svg>
  <div class="abs" style="left:86px;top:2023px;width:127px;height:102px;background:var(--sky)"></div>
  <div class="abs" role="img" aria-label="Photo of warehouse staff walking between tall shelving aisles" style="left:109px;top:2051px;width:370px;height:452px;clip-path:polygon(0 0,100% 0,100% 100%,0 86%);background:linear-gradient(160deg,#cfc6b6,#8c7c68 55%,#3d4a58)"></div>
  <div class="abs" style="left:996px;top:2431px;width:128px;height:103px;background:var(--navy)"></div>
  <div class="abs" style="left:479px;top:2051px;width:609px;height:452px;background:var(--white);border-left:7px solid var(--navy);box-shadow:0 6px 20px rgba(20,40,70,.1)">
    <div class="abs eyebrow-blue" style="left:62px;top:46px">WHO WE ARE</div>
    <div class="abs section-title" style="left:62px;top:76px">ABOUT TARVO FULFILMENT</div>
    <div class="abs" style="left:62px;top:132px;width:500px;font-size:12.5px;line-height:26px;font-weight:700;color:var(--blue)">Lorem ipsum dolor sit amet, consectetur adipiscing elit, sed do eiusmod tempor incididunt ut labore et dolore magna aliqua. Quis ommodo viverra maecenas accumsan lacus vel facilisis.</div>
    <div class="abs" style="left:62px;top:213px;width:510px;font-size:12.5px;line-height:27.5px;color:var(--grey)">Sed ut perspiciatis unde omnis iste natus error sit voluptatem accusantium doloremque laudantium, totam rem aperiam, eaque ipsa quae ab illo inventore totam rem aperiam, eaque ipsa quae ab illo inventore veritatis et quasi architecto beatae vitae m quia voluptas sit aspernatur aut odit aut fugit, sed quia consequu ntur magni dolores eos qui ratione voluptatem sequi nesciunt.</div>
    <div class="abs btn btn-dark" style="left:62px;top:363px;width:148px;height:50px;font-size:17px">READ MORE</div>
  </div>

  <div class="abs eyebrow-blue center" style="left:0;top:2578px;width:1200px">REVIEWS</div>
  <div class="abs section-title center" style="left:0;top:2610px;width:1200px">WHAT CUSTOMER SAYS</div>
  <div class="abs" role="img" aria-label="Customer portrait" style="left:520px;top:2679px;width:134px;height:134px;border-radius:50%;background:linear-gradient(180deg,#f4c59b,#2f2a2a)"></div>
  <div class="abs" role="img" aria-label="Customer portrait" style="left:116px;top:2752px;width:67px;height:67px;border-radius:50%;background:linear-gradient(180deg,#f6d9c4,#c4876a)"></div>
  <div class="abs" role="img" aria-label="Customer portrait" style="left:993px;top:2679px;width:47px;height:47px;border-radius:50%;background:linear-gradient(180deg,#e8d6cc,#5d4944)"></div>
  <div class="abs" style="left:360px;top:2790px;width:13px;height:13px;border-radius:50%;background:#e8262d"></div>
  <div class="abs" style="left:876px;top:2750px;width:7px;height:7px;border-radius:50%;background:var(--sky)"></div>
  <svg class="abs" style="left:148px;top:2858px" width="93" height="80" viewBox="0 0 93 80"><path d="M0 80V44C0 18 12 4 38 0v14C24 18 20 28 20 40h18v40zM55 80V44C55 18 67 4 93 0v14C79 18 75 28 75 40h18v40z" fill="#e3e3e3"/></svg>
  <svg class="abs" style="left:940px;top:2957px" width="93" height="83" viewBox="0 0 93 80"><path d="M93 0v36c0 26-12 40-38 44V66c14-4 18-14 18-26H55V0zM38 0v36C38 62 26 76 0 80V66c14-4 18-14 18-26H0V0z" fill="#e3e3e3"/></svg>
  <div class="abs head center" style="left:0;top:2835px;width:1200px;font-size:20px;font-weight:700;color:var(--ink)">Daniel Ferrow</div>
  <div class="abs center" style="left:0;top:2870px;width:1200px;font-size:12px;font-weight:700;color:var(--grey)">United States</div>
  <div class="abs center" style="left:0;top:2895px;width:1200px;font-size:31px;letter-spacing:1px;color:#f3a623">&#9733;&#9733;&#9733;&#9733;&#9733;</div>
  <div class="abs center" style="left:270px;top:2940px;width:660px;font-size:14.5px;line-height:26.5px;color:var(--grey)">Itaque earum rerum hic tenetur a sapiente delectus, ut aut reiciendis voluptatibus maiores alias. Consequatur aut perferendis doloribus asperiores repellat.Et harum quidem rerum facilis est et expedita distinctio.</div>
  <div class="abs" style="left:540px;top:3041px;display:flex;gap:8px">
    <span style="width:13px;height:13px;border-radius:50%;background:var(--pale)"></span><span style="width:13px;height:13px;border-radius:50%;background:var(--pale)"></span><span style="width:13px;height:13px;border-radius:50%;background:var(--pale)"></span><span style="width:13px;height:13px;border-radius:50%;background:var(--navy)"></span><span style="width:13px;height:13px;border-radius:50%;background:var(--pale)"></span><span style="width:13px;height:13px;border-radius:50%;background:var(--pale)"></span>
  </div>

  <div class="abs eyebrow-blue" style="left:112px;top:3158px">CONTACT US</div>
  <div class="abs section-title" style="left:109px;top:3190px">GET IN TOUCH WITH US</div>
  <div class="abs" style="left:112px;top:3247px;width:460px;font-size:13.5px;line-height:25px;color:var(--grey)">Dseste natus error sit voluptatem accusan tium doloremque laudantium, totam rem aperiam, ease aque ipaefdsa quae ab illo inventore veritatis ease totam rem aperiam, ease aque ipaefdsa quae ab illo inventore veritatis ease illo inventore veritatis ease quasi architecto.</div>
  <svg class="abs" style="left:111px;top:3369px" width="37" height="37" viewBox="0 0 37 37"><circle cx="18.5" cy="18.5" r="18.5" fill="var(--navy)"/><path d="M14.5 16.8a11 11 0 0 0 5 5l1.7-1.6c.2-.2.5-.3.8-.2.8.3 1.7.4 2.7.4.4 0 .8.3.8.8v2.6c0 .4-.4.8-.8.8A12.8 12.8 0 0 1 11.7 11.8c0-.4.3-.8.8-.8h2.6c.4 0 .8.4.8.8 0 1 .1 1.9.4 2.7 0 .3 0 .6-.2.8z" fill="#fff"/></svg>
  <div class="abs" style="left:167px;top:3372px;font-size:11px;color:var(--grey)">Call Us</div>
  <div class="abs" style="left:167px;top:3389px;font-size:13px;font-weight:700;color:var(--ink)">+1 555 010 0199</div>
  <svg class="abs" style="left:111px;top:3430px" width="37" height="37" viewBox="0 0 37 37"><circle cx="18.5" cy="18.5" r="18.5" fill="var(--navy)"/><rect x="10" y="13" width="17" height="12" rx="1.5" fill="#fff"/><path d="M10.5 13.5l8 6 8-6" stroke="var(--navy)" stroke-width="1.5" fill="none"/></svg>
  <div class="abs" style="left:167px;top:3432px;font-size:11px;color:var(--grey)">Email</div>
  <div class="abs" style="left:167px;top:3449px;font-size:13px;font-weight:700;color:var(--ink)">info@tarvofulfilment.com</div>

  <div class="abs field" style="left:676px;top:3130px;width:412px;height:42px">Your Name</div>
  <div class="abs field" style="left:676px;top:3190px;width:412px;height:42px">Email</div>
  <div class="abs field" style="left:676px;top:3250px;width:412px;height:42px">Phone Number</div>
  <div class="abs field" style="left:676px;top:3310px;width:412px;height:125px">Enter Your Message</div>
  <div class="abs btn btn-dark" style="left:676px;top:3451px;width:113px;height:47px;font-size:14px;border-radius:4px">SUBMIT &nbsp;&#8250;</div>

  <div class="abs" style="left:0;top:3564px;width:1200px;height:447px;background:var(--mist)"></div>
  <div class="abs brand-square" style="left:142px;top:3686px;width:50px;height:50px"></div>
  <div class="abs brand" style="left:109px;top:3748px;font-size:30px">TARVO FULFILMENT</div>
  <div class="abs social" style="left:110px;top:3808px"></div>
  <div class="abs social" style="left:168px;top:3808px"></div>
  <div class="abs social" style="left:227px;top:3808px"></div>
  <div class="abs social" style="left:284px;top:3808px"></div>

  <div class="abs footer-title" style="left:484px;top:3667px">QUICK LINKS</div>
  <ul class="abs footer-list" style="left:486px;top:3705px">
    <li><span style="color:var(--navy)">&#10140;</span>Home</li><li><span style="color:var(--navy)">&#10140;</span>About</li><li><span style="color:var(--navy)">&#10140;</span>Service</li><li><span style="color:var(--navy)">&#10140;</span>Testimonials</li><li><span style="color:var(--navy)">&#10140;</span>Contact Us</li>
  </ul>
  <div class="abs footer-title" style="left:685px;top:3667px">HELP LINKS</div>
  <ul class="abs footer-list" style="left:686px;top:3705px">
    <li><span style="color:var(--navy)">&#10140;</span>FAQ</li><li><span style="color:var(--navy)">&#10140;</span>Terms of use</li><li><span style="color:var(--navy)">&#10140;</span>Privacy Policy</li><li><span style="color:var(--navy)">&#10140;</span>Support Links</li><li><span style="color:var(--navy)">&#10140;</span>Conditions</li>
  </ul>
  <div class="abs footer-title" style="left:876px;top:3667px">CONTACT US</div>
  <svg class="abs" style="left:876px;top:3706px" width="33" height="33" viewBox="0 0 33 33"><circle cx="16.5" cy="16.5" r="16.5" fill="var(--navy)"/><path d="M16.5 8a5.5 5.5 0 0 0-5.5 5.5c0 4 5.5 10.5 5.5 10.5S22 17.5 22 13.5A5.5 5.5 0 0 0 16.5 8zm0 7.5a2 2 0 1 1 0-4 2 2 0 0 1 0 4z" fill="#fff"/></svg>
  <div class="abs" style="left:920px;top:3710px;font-size:14.5px;line-height:24px;color:var(--ink)">Tarvo Fulfilment<br>United States</div>
  <svg class="abs" style="left:876px;top:3776px" width="33" height="33" viewBox="0 0 37 37"><circle cx="18.5" cy="18.5" r="18.5" fill="var(--navy)"/><path d="M14.5 16.8a11 11 0 0 0 5 5l1.7-1.6c.2-.2.5-.3.8-.2.8.3 1.7.4 2.7.4.4 0 .8.3.8.8v2.6c0 .4-.4.8-.8.8A12.8 12.8 0 0 1 11.7 11.8c0-.4.3-.8.8-.8h2.6c.4 0 .8.4.8.8 0 1 .1 1.9.4 2.7 0 .3 0 .6-.2.8z" fill="#fff"/></svg>
  <div class="abs" style="left:920px;top:3783px;font-size:14.5px;color:var(--ink)">+1 555 010 0199</div>
  <svg class="abs" style="left:876px;top:3828px" width="33" height="33" viewBox="0 0 37 37"><circle cx="18.5" cy="18.5" r="18.5" fill="var(--navy)"/><rect x="10" y="13" width="17" height="12" rx="1.5" fill="#fff"/><path d="M10.5 13.5l8 6 8-6" stroke="var(--navy)" stroke-width="1.5" fill="none"/></svg>
  <div class="abs" style="left:920px;top:3835px;font-size:14.5px;color:var(--ink)">info@tarvofulfilment.com</div>

  <div class="abs" style="left:109px;top:3915px;width:979px;height:1px;background:var(--navy)"></div>
  <div class="abs center" style="left:0;top:3951px;width:1200px;font-size:14px;font-weight:700;color:var(--navy)">Copyrights@2023.Tarvo Fulfilment.All Rights Reserved</div>
</div>
</body>
</html>
```